Business Card Design Project

We have a logo, but would like to expand the use of it into a business card design. We are a B2B technology exchange platform for institutional investors to invest excess cash into short term assets matching their credit and pricing parameters. The assets are fractionalized and investors invest in portions.

Our customers are large, institutional, financial companies who are a bit traditional. We are high energy rebels with a cause...we are a disruptive technology and want to be viewed as a game changer but we need to present an image of trustworthiness and secure.

We are open not only to the image design but the material, die cut, etc. but want to stay in the traditional size of a business card.

We have other formats of the logo if needed. Our website is www.brambleharbor.com

I have posted a powerpoint template that we have been using.  This should not be considered the template we will use (after business cards we will have another project to incorporate business card design into powerpoint template) but just to give you a flavor of where we have been and have used in the past.

Target Market(s)

Institutional investors, asset managers, large fund institutions

Industry/Entity Type

Financial

Requirements
Must have
• Our logo
Traditional size
Nice to have
• unique use of logo, unique material, die cut, etc
Crisp, clean look
Use of both sides of card in a creative manner

```html
<!DOCTYPE html>
<html lang="en">
<head>
<meta charset="utf-8">
<title>Bramble Harbor – Business Card</title>
<link rel="stylesheet" href="https://fonts.googleapis.com/css2?family=Didact+Gothic&family=Montserrat:wght@600;700&display=swap">
<style>
  :root {
    --orange: #f7941d;
    --slate: #5f6062;
    --mist: #ebebeb;
    --ink: #3d3d3d;
    --white: #ffffff;
    --stage: #dcdcdc;
    --body-font: "Didact Gothic", "Century Gothic", sans-serif;
    --head-font: "Montserrat", "Century Gothic", sans-serif;
  }
  * { margin: 0; padding: 0; box-sizing: border-box; }
  html, body { width: 1200px; height: 506px; overflow: hidden; }
  body { background: var(--stage); position: relative; font-family: var(--body-font); color: var(--ink); }

  .card {
    position: absolute; top: 104px;
    width: 535px; height: 298px;
    overflow: hidden; background: var(--mist);
    box-shadow: 0 2px 6px rgba(0,0,0,.18);
  }
  .card--front { left: 50px; }
  .card--back { left: 615px; }
  .card__art {
    position: absolute; left: 0; top: 0;
    width: 625px; height: 348px;
    transform: scale(0.856); transform-origin: left top;
  }
  .card__shapes { position: absolute; inset: 0; width: 625px; height: 348px; display: block; }
  .fill-orange { fill: var(--orange); }
  .fill-slate { fill: var(--slate); }
  .fill-mist { fill: var(--mist); }

  .brand {
    position: absolute; width: 200px; height: 70px;
    display: flex; align-items: center; justify-content: center; gap: 10px;
  }
  .brand__name {
    font-family: var(--head-font); font-weight: 700; color: var(--slate);
    font-size: 27px; line-height: 0.95; letter-spacing: 0.5px; text-transform: uppercase;
  }
  .brand__dot { width: 20px; height: 20px; border-radius: 50%; background: var(--orange); flex: none; }
  .card--front .brand { left: 18px; top: 113px; transform: rotate(-19.5deg); }
  .card--back .brand { left: 415px; top: 108px; transform: rotate(19.5deg); }

  .identity {
    position: absolute; left: 258px; top: 100px;
    transform: rotate(-19.5deg); transform-origin: left top;
    white-space: nowrap;
  }
  .identity__name { font-family: var(--head-font); font-weight: 700; font-size: 24px; color: var(--white); line-height: 28px; }
  .identity__title { font-size: 20px; color: var(--mist); line-height: 24px; }

  .contact { list-style: none; margin: 24px 0 0 12px; }
  .contact__item { display: flex; align-items: center; gap: 10px; font-size: 16px; line-height: 18px; color: var(--ink); }
  .contact__icon { width: 11px; height: 11px; flex: none; }
  .contact__icon * { fill: none; stroke: var(--orange); stroke-width: 1.3; }
  .contact__icon .solid { fill: var(--orange); stroke: none; }

  .address { font-style: normal; font-size: 14px; line-height: 16px; margin: 14px 0 0 34px; color: var(--ink); }

  .slogan {
    position: absolute; right: 242px; top: 80px;
    transform: rotate(19.5deg); transform-origin: right top;
    font-family: var(--head-font); font-weight: 700; font-size: 19px; line-height: 24px;
    color: var(--white); text-align: right; white-space: nowrap;
  }
  .mission {
    position: absolute; left: 27px; top: 100px;
    transform: rotate(19.5deg); transform-origin: left top;
    font-size: 16px; line-height: 17.5px; color: var(--ink); white-space: nowrap;
  }
  .mission__line { display: block; }
  .mission__line:nth-child(2) { padding-left: 6px; }
  .mission__line:nth-child(3) { padding-left: 12px; }
  .mission__line:nth-child(4) { padding-left: 18px; }
  .mission__line:nth-child(5) { padding-left: 24px; }
  .mission__line:nth-child(6) { padding-left: 30px; }
  .mission__line:nth-child(7) { padding-left: 36px; }
</style>
</head>
<body>

<section class="card card--front" aria-label="Business card front">
  <div class="card__art">
    <svg class="card__shapes" viewBox="0 0 625 348" aria-hidden="true">
      <rect class="fill-mist" width="625" height="348"/>
      <polygon class="fill-orange" points="0,0 210,0 305,348 0,348"/>
      <polygon class="fill-mist" points="0,116 226,38 278,173 0,253"/>
      <polygon class="fill-slate" points="210,0 625,0 625,50 278,173"/>
    </svg>

    <div class="brand">
      <span class="brand__name">Bramble<br>Harbor</span>
      <span class="brand__dot"></span>
    </div>

    <div class="identity">
      <p class="identity__name">Martin Ellsworth</p>
      <p class="identity__title">President &amp; CEO</p>
      <ul class="contact">
        <li class="contact__item">
          <svg class="contact__icon" viewBox="0 0 10 10"><path d="M2 1 L4 3 L3 4.5 Q4.5 6.5 5.5 7 L7 6 L9 8 L7.5 9.3 Q3 8 0.8 2.5 Z"/></svg>
          555.210.4418
        </li>
        <li class="contact__item">
          <svg class="contact__icon" viewBox="0 0 10 10"><rect x="2.5" y="0.8" width="5" height="8.4" rx="0.8"/><circle class="solid" cx="5" cy="7.8" r="0.6"/></svg>
          555.382.7701
        </li>
        <li class="contact__item">
          <svg class="contact__icon" viewBox="0 0 10 10"><rect x="0.8" y="2" width="8.4" height="6"/><path d="M0.8 2 L5 5.5 L9.2 2"/></svg>
          martin@brambleharbor.com
        </li>
        <li class="contact__item">
          <svg class="contact__icon" viewBox="0 0 10 10"><circle cx="5" cy="5" r="4.2"/><path d="M0.8 5 H9.2 M5 0.8 Q2.5 5 5 9.2 M5 0.8 Q7.5 5 5 9.2"/></svg>
          www.brambleharbor.com
        </li>
        <li class="contact__item">
          <svg class="contact__icon" viewBox="0 0 10 10"><rect x="0.8" y="0.8" width="8.4" height="8.4"/></svg>
          martinellsworth
        </li>
      </ul>
      <address class="address">2210 Harbor Crest Drive<br>Suite 118<br>Millbrook, CA 90210</address>
    </div>
  </div>
</section>

<section class="card card--back" aria-label="Business card back">
  <div class="card__art">
    <svg class="card__shapes" viewBox="0 0 625 348" aria-hidden="true">
      <rect class="fill-mist" width="625" height="348"/>
      <polygon class="fill-orange" points="430,0 625,0 625,348 320,348"/>
      <polygon class="fill-mist" points="625,113 415,40 375,171 625,253"/>
      <polygon class="fill-slate" points="0,0 430,0 375,171 0,53"/>
    </svg>

    <p class="slogan">Your slogan Your<br>Your slogan Your slogan Your</p>

    <p class="mission">
      <span class="mission__line">Bramble Harbor transforms the old relationship</span>
      <span class="mission__line">lending paradigm into a powerful,</span>
      <span class="mission__line">institutional crowd sourcing platform</span>
      <span class="mission__line">where ecosystem participants can</span>
      <span class="mission__line">perform and gain reputational rewards</span>
      <span class="mission__line">in an environment which requires no</span>
      <span class="mission__line">long term commitment.</span>
    </p>

    <div class="brand">
      <span class="brand__name">Bramble<br>Harbor</span>
      <span class="brand__dot"></span>
    </div>
  </div>
</section>

</body>
</html>
```